Harbin Cargo needs a business card design.

Design a double-sided business card for new freight business. On the front, would like to see our logo along with the following info:

Nathaniel Voskuhl
CEO/FOUNDER
617-552-0194
nathanielvoskuhl@harbin-cargo.example

On the reverse side, we would like to use the graphic image of our logo only without the Harbin Cargo name.

```html
<!DOCTYPE html>
<html lang="en">
<head>
<meta charset="utf-8">
<title>Harbin Cargo – Business Card</title>
<link rel="stylesheet" href="https://fonts.googleapis.com/css2?family=Mulish:wght@400;700;800&display=swap">
<style>
  :root {
    --navy: #1b1a55;
    --navy-soft: #262570;
    --red: #b81e25;
    --ink: #3a3a3a;
    --paper: #ffffff;
    --backdrop: #dcdde1;
  }
  * { margin: 0; padding: 0; box-sizing: border-box; }
  html, body {
    width: 1200px; height: 859px; overflow: hidden;
    background: var(--backdrop);
    font-family: "Mulish", sans-serif;
  }
  .stage { position: relative; width: 1200px; height: 859px; }
  .card {
    position: absolute; left: 319px; width: 562px; height: 321px;
  }
  .card--front { top: 69px; background: var(--paper); }
  .card--back { top: 470px; background: var(--navy); }

  .wordmark {
    position: absolute; top: 40px; right: 27px;
    display: flex; align-items: center; gap: 16px;
  }
  .wordmark__square { width: 62px; height: 62px; background: var(--red); flex: none; }
  .wordmark__name {
    font-weight: 800; font-size: 27px; letter-spacing: 6px;
    color: var(--navy); text-transform: uppercase; line-height: 1.08;
    width: 180px;
  }

  .identity { position: absolute; left: 0; top: 195px; }
  .identity__bar {
    position: absolute; left: 0; top: 0; width: 11px; height: 30px; background: var(--red);
  }
  .identity__name {
    position: absolute; left: 22px; top: -4px; white-space: nowrap;
    font-weight: 800; font-size: 20px; color: var(--navy);
  }
  .identity__name .surname { color: var(--red); }
  .identity__role {
    position: absolute; left: 22px; top: 19px; white-space: nowrap;
    font-size: 12px; color: var(--ink); letter-spacing: 0.2px;
  }

  .contacts {
    position: absolute; left: 22px; top: 244px; list-style: none;
  }
  .contacts li {
    display: flex; align-items: center; gap: 6px;
    font-size: 13px; color: var(--ink); height: 18px;
  }
  .contacts svg { width: 11px; height: 11px; fill: var(--red); flex: none; }

  .back-mark {
    position: absolute; left: 50%; top: 50%; transform: translate(-50%, -50%);
    width: 150px; height: 150px;
    background: linear-gradient(135deg, #2e2d7a 0%, #1f1e5e 100%);
  }
</style>
</head>
<body>
<main class="stage">
  <section class="card card--front" aria-label="Business card front">
    <div class="wordmark">
      <span class="wordmark__square"></span>
      <span class="wordmark__name">Harbin Cargo</span>
    </div>

    <div class="identity">
      <span class="identity__bar"></span>
      <h1 class="identity__name">Nathaniel <span class="surname">Voskuhl</span></h1>
      <p class="identity__role">CEO/FOUNDER</p>
    </div>

    <ul class="contacts">
      <li>
        <svg viewBox="0 0 24 24" aria-hidden="true"><path d="M6.6 10.8a15.1 15.1 0 0 0 6.6 6.6l2.2-2.2c.3-.3.7-.4 1-.2 1.1.4 2.3.6 3.6.6.6 0 1 .4 1 1V20c0 .6-.4 1-1 1A17 17 0 0 1 3 4c0-.6.4-1 1-1h3.5c.6 0 1 .4 1 1 0 1.3.2 2.5.6 3.6.1.3 0 .7-.2 1z"/></svg>
        617-552-0194
      </li>
      <li>
        <svg viewBox="0 0 24 24" aria-hidden="true"><path d="M2 5h20v14H2z M2 5l10 8 10-8" fill="var(--red)" stroke="#fff" stroke-width="1.5"/></svg>
        nathanielvoskuhl@harbin-cargo.example
      </li>
      <li>
        <svg viewBox="0 0 24 24" aria-hidden="true"><circle cx="12" cy="12" r="10"/><path d="M7 7c2 1 3 3 2 5s1 3 2 5M15 4c-1 2 0 3 2 4s3 2 2 4" stroke="#fff" stroke-width="1.5" fill="none"/></svg>
        www.harbin-cargo.example
      </li>
    </ul>
  </section>

  <section class="card card--back" aria-label="Business card back">
    <span class="back-mark" role="img" aria-label="Company mark placeholder"></span>
  </section>
</main>
</body>
</html>
```